verdant terraces simple classy business card design

my name is owen harlow and I run a gardening business aimed at high class verdant terraces. the business name is verdant terraces and our logo was designed on pixel forum .My clientel are anything from residential homes to businesses. I take pride in my work and know that I offer a service like no other in my area.
The business card will be used to represent my business and I want it to be not only rememberable, but simplistic and modern. Eye catching too. Of course I would like it relatable to gardening and appealing to the correct clientel - those being garden enthusiasts, prestigious homes and businesses that are after top of the line gardening services like no other on the market.
I am not a typical lawn mowing business so I don't want a typical card design that represents that. The gardens I work with are generally million dollar properties with owners who are very garden proud looking for upkeep and guidance from me along with sometimes whole new garden designs. I want the business cards to show to my clients that I take pride, as they do, in their garden. And I want them to know from my card that I am a professional, qualified horticulturist offering them a top of the line service for life. I want them to refer my business on. I want them to look at my business card and see class and professionalism in a modern unique bold way.
The card should be simple with the possibility of the logo on the front being embossed/debossed and my details on the back the card should have a organic garden feel it's very important to me that it is absolutely perfect
I am also very open to ideas and suggestions so look forward to seeing the designs. the business logo has been supplied with this project and I want the card to be double sided

Contact info is
Owen Harlow - Managing Director / Horticulturist
Phone : 0481 526 704
Email: owenharlow@verdantterraces.com.au

Target Market(s)

high class gardens residential and commercial

Industry/Entity Type

Gardener

Contact Information for Business Card

Contact info is
Phone : 0481 526 704

PLEASE MAKE CARD DOUBLE SIDED

Requirements
Must have
• organic simple classy modern feel
• must flow with the current logo that has been supplied with this project
• Double sided
• Must explain in a simple way that I deal with high end gardens and I'm a qualified horticulturist
Nice to have
• embossed debossed logo
Should not have
• shouldn't be to busy or cheap looking

```html
<!DOCTYPE html>
<html lang="en">
<head>
<meta charset="utf-8">
<title>Verdant Terraces – Business Card</title>
<link href="https://fonts.googleapis.com/css2?family=Cinzel:wght@400;500&family=Open+Sans:wght@400&display=swap" rel="stylesheet">
<style>
  :root {
    --page-bg: #d9dbd9;
    --card-white: #ffffff;
    --brand-green: #4f9152;
    --green-light: #5c9b5e;
    --green-dark: #3e7a43;
    --leaf-dark: #2f6435;
    --text-light: #f4f8f2;
    --rule-light: rgba(255,255,255,0.35);
  }
  * { box-sizing: border-box; margin: 0; padding: 0; }
  html, body {
    width: 1200px; height: 1200px; overflow: hidden;
    background: var(--page-bg);
  }
  .sheet {
    width: 1200px; height: 1200px;
    display: flex; flex-direction: column;
    align-items: center; justify-content: center; gap: 56px;
  }
  .card {
    width: 900px; height: 514px; position: relative; overflow: hidden;
    box-shadow: 0 6px 22px rgba(0,0,0,0.18);
  }

  /* Front */
  .card-front {
    background: var(--card-white);
    display: flex; flex-direction: column; align-items: center; justify-content: center;
  }
  .brand-name {
    font-family: "Cinzel", serif; font-weight: 500; color: var(--brand-green);
    text-align: center; line-height: 1;
  }
  .brand-name .word-main { display: block; font-size: 88px; letter-spacing: 2px; }
  .brand-name .word-sub { display: block; font-size: 48px; letter-spacing: 40px; margin-top: 14px; padding-left: 40px; }

  /* Back */
  .card-back {
    background: linear-gradient(160deg, var(--green-light) 0%, var(--green-dark) 100%);
    color: var(--text-light);
  }
  .contact-block {
    position: absolute; left: 150px; top: 92px; width: 470px; text-align: center;
  }
  .contact-name {
    font-family: "Cinzel", serif; font-weight: 400; font-size: 40px; letter-spacing: 2px;
  }
  .contact-role {
    font-family: "Open Sans", sans-serif; font-size: 18px; margin-top: 6px;
    padding-bottom: 22px; border-bottom: 1px solid var(--rule-light);
  }
  .contact-details {
    font-family: "Open Sans", sans-serif; font-size: 18px; letter-spacing: 0.3px; margin-top: 18px;
    white-space: nowrap;
  }
  .contact-details .sep { margin: 0 8px; }
  .garden-illustration {
    position: absolute; left: 0; bottom: 0; width: 900px; height: 230px;
  }
</style>
</head>
<body>
<main class="sheet">
  <section class="card card-front" aria-label="Card front">
    <h1 class="brand-name">
      <span class="word-main">VERDANT</span>
      <span class="word-sub">TERRACES</span>
    </h1>
  </section>

  <section class="card card-back" aria-label="Card back">
    <div class="contact-block">
      <p class="contact-name">OWEN HARLOW</p>
      <p class="contact-role">Managing Director / Horticulturist</p>
      <p class="contact-details">0481 526 704<span class="sep">|</span>owenharlow@verdantterraces.com.au</p>
    </div>
    <svg class="garden-illustration" viewBox="0 0 900 230" role="img" aria-label="Illustration of rounded leafy trees along a rolling green hill">
      <defs>
        <linearGradient id="hill-fill" x1="0" y1="0" x2="1" y2="1">
          <stop offset="0" stop-color="#3f7b44" stop-opacity="0"/>
          <stop offset="0.5" stop-color="#356f3b" stop-opacity="0.55"/>
          <stop offset="1" stop-color="#2f6435" stop-opacity="0.8"/>
        </linearGradient>
      </defs>
      <rect x="0" y="0" width="900" height="230" fill="url(#hill-fill)"/>
    </svg>
  </section>
</main>
</body>
</html>
```